Willow’s Lantern - Childhood Cancer Journey

In 2019, Corbin, my five-year-old, was diagnosed with stage 4 kidney cancer.

From the beginning, I said God would do his part, the doctors will do theirs, and I would do mine to save my son.

Diving into Christian beliefs and research, I learned and applied major shifts in everything we didn’t. Pulling invaluable information from fields like alternative cancer treatments coupled with Tall Reed study, Longevity, Biohacking, Functional Medicine, and microbiome.

Corbin when from stage 4 to cancer-free in 8 months. The journey is and was very difficult, but we’ve learned and been able to help countless others.

Industry/Entity Type

Health, Wellness, Mindset, Adversity

Requirements
Nice to have
• Bright with feelings of warmth

```html
<!DOCTYPE html>
<html lang="en">
<head>
<meta charset="UTF-8">
<title>Willow’s Lantern – Childhood Cancer Journey</title>
<link href="https://fonts.googleapis.com/css2?family=Montserrat:wght@500;600;800&family=Sniglet:wght@400;800&display=swap" rel="stylesheet">
<style>
  :root {
    --page-bg: #f3f4f5;
    --cover-white: #ffffff;
    --navy: #0e3f5c;
    --band-blue: #0b4a6b;
    --teal: #3aafbf;
    --ink: #1f2a30;
    --text-light: #ffffff;
    --produce-green: #8dbf5a;
    --produce-red: #e0523f;
    --produce-orange: #f2a13a;
    --produce-yellow: #f3d45a;
    --produce-pink: #e04a7e;
  }
  * { box-sizing: border-box; margin: 0; padding: 0; }
  html, body {
    width: 1200px; height: 816px; overflow: hidden;
    background: var(--page-bg);
  }
  .canvas {
    position: relative; width: 1200px; height: 816px;
    display: flex; align-items: center; justify-content: center;
  }
  .cover {
    position: relative; width: 520px; height: 780px;
    background: var(--cover-white);
    overflow: hidden;
    box-shadow: 0 6px 24px rgba(0,0,0,0.12);
  }
  .produce {
    position: absolute; opacity: 0.85; z-index: 1;
  }
  .produce--top {
    top: 0; left: 0; width: 520px; height: 92px;
    background: linear-gradient(90deg, var(--produce-red), var(--produce-green) 25%, var(--produce-yellow) 45%, var(--produce-orange) 60%, var(--produce-red) 78%, var(--produce-green));
    border-radius: 0 0 40px 40px;
  }
  .produce--left {
    top: 100px; left: 0; width: 84px; height: 360px;
    background: linear-gradient(180deg, var(--produce-green), var(--produce-orange) 35%, var(--produce-red) 65%, var(--produce-pink));
    border-radius: 0 40px 40px 0;
  }
  .produce--right {
    top: 100px; right: 0; width: 84px; height: 360px;
    background: linear-gradient(180deg, var(--produce-pink), var(--produce-green) 35%, var(--produce-green) 65%, var(--produce-orange));
    border-radius: 40px 0 0 40px;
  }
  .author {
    position: absolute; top: 120px; left: 0; width: 100%;
    text-align: center;
    font-family: 'Montserrat', sans-serif; font-weight: 800;
    font-size: 27px; letter-spacing: 1px; color: var(--navy);
  }
  .author-rule {
    position: absolute; top: 170px; left: 235px; width: 50px; height: 2px;
    background: var(--navy);
  }
  .title {
    position: absolute; top: 188px; left: 0; width: 100%;
    text-align: center; font-family: 'Sniglet', sans-serif; font-weight: 800;
    line-height: 0.95;
  }
  .title-first { display: block; font-size: 66px; color: var(--teal); }
  .title-second { display: block; font-size: 72px; color: var(--navy); }
  .subtitle {
    position: absolute; top: 352px; left: 0; width: 100%;
    text-align: center; font-family: 'Montserrat', sans-serif; font-weight: 600;
    font-size: 21px; line-height: 1.1; color: var(--ink);
  }
  .band {
    position: absolute; left: 0; top: 468px; width: 100%; height: 312px;
    background: var(--band-blue);
    z-index: 2;
  }
  .portrait {
    position: absolute; left: 185px; top: 420px; width: 150px; height: 150px;
    border-radius: 50%; border: 6px solid var(--cover-white);
    background: radial-gradient(circle at 40% 45%, #d9a27a, #b84a3d 55%, #6b4a35);
    z-index: 4;
  }
  .tagline {
    position: absolute; left: 50px; top: 600px; width: 420px;
    font-family: 'Montserrat', sans-serif; font-weight: 600;
    font-size: 14px; line-height: 1.45; letter-spacing: 0.5px;
    text-transform: uppercase; text-align: center; color: var(--text-light);
    z-index: 4;
  }
</style>
</head>
<body>
  <div class="canvas">
    <div class="cover">
      <div class="produce produce--top" role="img" aria-label="Hand-drawn border of fruit and vegetables"></div>
      <div class="produce produce--left" role="img" aria-label="Hand-drawn carrots, tomato and dragon fruit"></div>
      <div class="produce produce--right" role="img" aria-label="Hand-drawn radish, cauliflower, broccoli, lettuce and beans"></div>

      <div class="author">NOLAN AVERY</div>
      <div class="author-rule"></div>

      <h1 class="title">
        <span class="title-first">Willow’s</span>
        <span class="title-second">Lantern</span>
      </h1>
      <p class="subtitle">Childhood<br>Cancer Journey</p>

      <div class="band"></div>
      <div class="portrait" role="img" aria-label="Photo of a father and his young son preparing fruit in a kitchen"></div>
      <p class="tagline">A loving father, determined to guide his cancer-stricken son Corbin’s journey to a cure, discovers the Tall Reed protocol of nourishing the body to optimum health</p>
    </div>
  </div>
</body>
</html>
```